HTML newsletter template for construction company

Hello. I need a company newsletter template made. Our website is: www.halvernbuildco.com

Can you please spend some time on our website and design a similarly themed newsletter template for us? We use infusionsoft, so it'd be great if someone has experience with infusionsoft's newsletter requirements.

Target Market(s)

All sized subcontracting companies. We are a national company but are headquartered in Phoenix, Az.

Industry/Entity Type

Construction Company

Font styles to use
Sans Serif

Requirements
Must have
• html
Nice to have
• We need a few different "sections" for content. We're planning on having an interview, a construction project spotlight, some type of article, tips of some-sort and provide a few upcoming events that we are participating in.

```html
<!DOCTYPE html>
<html lang="en">
<head>
<meta charset="utf-8">
<title>Halvern BuildCo Newsletter</title>
<link href="https://fonts.googleapis.com/css2?family=Roboto:wght@300;400;500;700&display=swap" rel="stylesheet">
<style>
:root{
  --ink:#222;
  --text:#333;
  --orange:#e8661b;
  --dark:#2b2b2b;
  --darker:#1f1f1f;
  --grey:#ececec;
  --white:#fff;
}
*{box-sizing:border-box;margin:0;padding:0}
html,body{width:831px;height:1200px;overflow:hidden;background:var(--white)}
body{font-family:'Roboto',Arial,sans-serif;color:var(--text);position:relative}
.masthead{position:absolute;top:0;left:0;width:831px;height:85px;background:var(--dark);display:flex;align-items:center;padding-left:36px;gap:12px}
.brand-dot{width:34px;height:34px;border-radius:50%;background:var(--white)}
.brand-name{color:var(--white);font-size:26px;font-weight:500}
.hero{position:absolute;top:85px;left:0;width:831px;height:345px;background:linear-gradient(90deg,#f4f3f1 0%,#e9e5df 50%,#b9a88e 100%)}
.hero-photo{position:absolute;top:0;right:0;width:420px;height:345px;background:linear-gradient(135deg,#d8cdbb,#9c8566 60%,#3b4d73)}
.hero-title{position:absolute;left:32px;top:170px;font-weight:300}
.hero-title .lead{display:block;font-size:56px;color:var(--ink);line-height:1}
.hero-title .accent{display:block;font-size:64px;color:var(--orange);font-weight:400;line-height:1.1}
.main{position:absolute;top:445px;left:0;width:831px;height:310px}
.spotlight{position:absolute;left:36px;width:520px}
.spotlight h2{font-size:21px;font-weight:700;color:var(--ink);margin-bottom:4px}
.spotlight p{font-size:14px;line-height:1.35}
.side{position:absolute;left:572px;top:8px;width:225px;background:var(--grey);height:302px;padding:12px}
.side-photo{width:201px;height:112px;border:6px solid var(--white);background:linear-gradient(135deg,#8a7e6b,#c9b894 50%,#5c5348)}
.side h3{color:var(--orange);font-size:21px;font-weight:400;margin:12px 0 5px}
.side p{font-size:13px;line-height:1.35;color:var(--text)}
.features{position:absolute;top:755px;left:0;width:831px;height:235px;background:var(--grey)}
.card{position:absolute;top:14px;background:var(--white);height:206px;padding:14px}
.card.interview{left:36px;width:515px;display:flex;gap:16px}
.card.events{left:563px;width:234px}
.portrait{width:155px;height:170px;flex:none;background:linear-gradient(160deg,#dcdcdc,#8d8d8d)}
.card h3{color:var(--orange);font-size:22px;font-weight:400;margin-bottom:6px}
.card p{font-size:13.5px;line-height:1.35;margin-bottom:10px}
.card .more{font-size:13px;font-weight:700;color:var(--ink)}
.signup{position:absolute;top:1000px;left:0;width:831px;height:72px;background:var(--orange);display:flex;align-items:center;justify-content:space-between;padding:0 36px}
.signup span{color:var(--white);font-size:23px}
.signup .btn{background:var(--dark);color:var(--white);font-size:18px;font-weight:700;padding:12px 36px;border-radius:3px}
.footer{position:absolute;top:1072px;left:0;width:831px;height:128px;background:var(--dark);color:#ddd;font-size:17px}
.contact{position:absolute;display:flex;align-items:center;gap:12px}
.contact svg{width:22px;height:22px}
.follow .sq{width:16px;height:16px;background:#777;display:inline-block}
.copyright{position:absolute;left:0;bottom:0;width:831px;height:26px;background:var(--darker);font-size:11px;color:#999;padding:7px 36px}
</style>
</head>
<body>
<header class="masthead">
  <span class="brand-dot"></span><span class="brand-name">Halvern BuildCo</span>
</header>

<section class="hero">
  <div class="hero-photo" role="img" aria-label="Construction worker in hard hat at a lumber yard"></div>
  <h1 class="hero-title"><span class="lead">A Desire For</span><span class="accent">Change</span></h1>
</section>

<section class="main">
  <article class="spotlight" style="top:8px">
    <h2>Spotlight</h2>
    <p>We provide the trade credit that gives contractors a repayment term of up to 150 days while covering the costs of their supply expenses in 10 days or less. This not only helps the contractors, but helps suppliers as well!</p>
  </article>
  <article class="spotlight" style="top:112px">
    <h2>Spotlight</h2>
    <p>Financial stress and limited business capabilities are destroying construction professionals. By supporting the financial needs of these companies, we're building better, stronger businesses. When business is strong and stable, construction companies can do amazing things. They are the ones who will literally build our future and build better communities for us to be a part of. We're not only building better lives for contractors and their families, but also impacting the population at large through positive economic, functional improvements that our support helps create.</p>
  </article>
  <aside class="side">
    <div class="side-photo" role="img" aria-label="Builder working on a timber frame"></div>
    <h3>News</h3>
    <p>Lorem Ipsum is simply dummy text of the printing and typesetting industry. Lorem Ipsum has been the industry's standard dummy text ever since the 1500s</p>
  </aside>
</section>

<section class="features">
  <article class="card interview">
    <div class="portrait" role="img" aria-label="Portrait of interviewed business owner"></div>
    <div>
      <h3>Interview</h3>
      <p>Lorem Ipsum is simply dummy text of the printing and typesetting industry. Lorem Ipsum has been the industry's standard dummy text ever since the 1500s</p>
      <span class="more">Read more.....</span>
    </div>
  </article>
  <article class="card events">
    <h3>Upcoming Events</h3>
    <p>Lorem Ipsum is simply dummy text of the printing and typesetting industry. Lorem Ipsum has been the industry's standard dummy text ever since the 1500s</p>
    <span class="more">Read more.....</span>
  </article>
</section>

<section class="signup">
  <span>Sign Up for Resources and Exclusive Events</span>
  <span class="btn">Sign Me Up!</span>
</section>

<footer class="footer">
  <div class="contact" style="left:36px;top:16px">
    <svg viewBox="0 0 24 24"><path fill="#ccc" d="M6.6 10.8a15 15 0 0 0 6.6 6.6l2.2-2.2c.3-.3.7-.4 1-.2 1.1.4 2.3.6 3.6.6.6 0 1 .4 1 1V20c0 .6-.4 1-1 1C10.6 21 3 13.4 3 4c0-.6.4-1 1-1h3.5c.6 0 1 .4 1 1 0 1.3.2 2.5.6 3.6.1.3 0 .7-.2 1z"/></svg>
    <span>+1 (866) 555-0142</span>
  </div>
  <div class="contact" style="left:36px;top:54px">
    <svg viewBox="0 0 24 24"><path fill="#ccc" d="M20 4H4a2 2 0 0 0-2 2v12a2 2 0 0 0 2 2h16a2 2 0 0 0 2-2V6a2 2 0 0 0-2-2zm0 4-8 5-8-5V6l8 5 8-5z"/></svg>
    <span>info@halvernbuildco.com</span>
  </div>
  <div class="contact" style="left:520px;top:16px">
    <svg viewBox="0 0 24 24"><circle cx="12" cy="12" r="9" fill="none" stroke="#ccc" stroke-width="2"/><path d="M3 12h18M12 3c3 3 3 15 0 18M12 3c-3 3-3 15 0 18" fill="none" stroke="#ccc" stroke-width="1.5"/></svg>
    <span>www.halvernbuildco.com</span>
  </div>
  <div class="contact follow" style="left:640px;top:54px">
    <span>Follow:</span><span class="sq"></span><span class="sq"></span><span class="sq"></span><span class="sq"></span>
  </div>
  <div class="copyright">Copyright © 2016 Halvern BuildCo. All Rights Reserved</div>
</footer>
</body>
</html>
```